Business Card for Bright Meadow Lawn & Landscape

Double Sided Card Design - I think one side of the card should be cleaner, with logo, contact info, and "Complete Residential & Commercial Landscape Services", and on the other side it should list the services we offer:

- Lawn Care & Mowing
- Hedge & Shrub Trimming
- Leaf Removal & Clean Up
- Aeration & Sod
- Mulch & Rock Installations
- Landscape Installations & Renovations
- Commercial Snow Removal

Please make it clean and very professional... don't want it too be too busy, but want to tell them what we do.

Target Market(s)

Residential and Commercial

Industry/Entity Type

Landscape

Contact Information for Business Card

Fully Insured
Tom Berrigan
410-555-0198
Tberrigan07@mailbox-example.com

Requirements
Must have
• Double Sided, Cleaner on one side, more information and text on the other side.

```html
<!DOCTYPE html>
<html lang="en">
<head>
<meta charset="utf-8">
<title>Bright Meadow Lawn &amp; Landscape — Business Card</title>
<link rel="stylesheet" href="https://fonts.googleapis.com/css2?family=Zilla+Slab:ital,wght@0,600;1,400&display=swap">
<style>
  :root {
    --page: #ece7df;
    --card: #070707;
    --green: #8cc63f;
    --green-deep: #79b531;
    --white: #f5f5f5;
  }
  * { box-sizing: border-box; margin: 0; padding: 0; }
  html, body { width: 1200px; height: 1200px; overflow: hidden; }
  body {
    background: var(--page);
    display: flex;
    flex-direction: column;
    align-items: center;
    justify-content: center;
    gap: 56px;
  }
  .card {
    position: relative;
    width: 900px;
    height: 514px;
    background: var(--card);
    color: var(--white);
    overflow: hidden;
    box-shadow: 0 10px 30px rgba(0,0,0,.18);
    font-family: "Zilla Slab", serif;
  }
  .band {
    position: absolute;
    left: 0; right: 0;
    top: 372px;
    height: 96px;
    background: linear-gradient(90deg, var(--green-deep), var(--green));
  }

  /* Front side */
  .brand-name {
    position: absolute;
    left: 88px;
    top: 84px;
    font-weight: 600;
    color: var(--green);
    font-size: 30px;
    line-height: 1.2;
  }
  .tagline {
    position: absolute;
    left: 88px;
    top: 258px;
    font-style: italic;
    font-size: 21px;
    line-height: 1.35;
  }
  .contact {
    position: absolute;
    left: 470px;
    top: 196px;
    padding-left: 22px;
    border-left: 2px solid var(--green);
    white-space: nowrap;
  }
  .contact__name {
    font-weight: 600;
    color: var(--green);
    font-size: 34px;
    letter-spacing: .5px;
    text-transform: uppercase;
  }
  .contact__note { font-style: italic; font-size: 18px; margin-bottom: 16px; }
  .contact__row { font-size: 18px; line-height: 1.55; display: flex; }
  .contact__label { color: var(--green); font-style: italic; width: 56px; }

  /* Back side */
  .wordmark {
    position: absolute;
    left: 0; right: 0;
    top: 92px;
    text-align: center;
    font-weight: 600;
    color: var(--green);
    font-size: 46px;
    line-height: 1.1;
  }
  .services {
    position: absolute;
    left: 40px; right: 40px;
    top: 222px;
    text-align: center;
    font-style: italic;
    font-size: 21px;
    line-height: 1.6;
  }
</style>
</head>
<body>
  <section class="card card--front" aria-label="Card front">
    <p class="brand-name">Bright Meadow<br>Lawn &amp; Landscape</p>
    <p class="tagline">Complete Residential &amp;<br>Commercial Landscape Services</p>
    <div class="contact">
      <p class="contact__name">Tom Berrigan</p>
      <p class="contact__note">Fully Insured</p>
      <p class="contact__row"><span class="contact__label">Tel</span>: 410-555-0198</p>
      <p class="contact__row"><span class="contact__label">Email</span>: Tberrigan07@mailbox-example.com</p>
    </div>
    <div class="band"></div>
  </section>

  <section class="card card--back" aria-label="Card back">
    <p class="wordmark">Bright Meadow Lawn &amp; Landscape</p>
    <p class="services">
      Lawn Care &amp; Mowing | Hedge &amp; Shrub Trimming | Leaf Removal &amp; Clean Up<br>
      Aeration &amp; Sod | Mulch &amp; Rock Installations | Landscape Installations &amp; Renovations<br>
      Commercial Snow Removal
    </p>
    <div class="band"></div>
  </section>
</body>
</html>
```